LED Bannerwerbung im Fußballstadion des SV Blitzhafen Murnau!
Zielgruppe
Die welmora hotels & resorts GmbH ist ein mittelständisches Familienunternehmen mit aktuell 25 Hotelbetreiben und ist Sponsor des SV Blitzhafen Murnau.
Aufgabenstellung
Wir haben eine LED Bandenwerbung in den Massen 4608px x 80px und möchten diese erneuern.
Längere Standzeit Logo - Animation ja aber nicht so lange. Witzig und spritzig . Im Kern sind wir
Spezialisten für Kurztrips im Osten.

```html
<!DOCTYPE html>
<html lang="de">
<head>
<meta charset="utf-8">
<title>welmora hotels &amp; resorts – LED-Bande</title>
<link rel="stylesheet" href="https://fonts.googleapis.com/css2?family=Ubuntu:wght@400;700&family=Montserrat:wght@700;800&family=Kaushan+Script&display=swap">
<style>
  :root {
    --stage: #6e6e6e;
    --band: #ffffff;
    --brand-green: #6fb52c;
    --brand-blue: #1d8fd1;
    --brand-orange: #f0821e;
    --sun: #f6a623;
    --sea: #2a7fc1;
    --palm: #7cc242;
  }
  * { box-sizing: border-box; margin: 0; padding: 0; }
  html, body { width: 1200px; height: 1117px; overflow: hidden; }
  body {
    background: var(--stage);
    display: flex;
    flex-direction: column;
    justify-content: center;
    align-items: center;
    gap: 10px;
  }
  .led-band {
    width: 1158px;
    height: 20px;
    background: var(--band);
    display: flex;
    align-items: center;
    overflow: hidden;
    white-space: nowrap;
  }
  .brand-unit {
    display: flex;
    align-items: center;
    flex: 0 0 auto;
    height: 100%;
  }
  .art {
    display: block;
    height: 18px;
    border-radius: 3px;
    flex: 0 0 auto;
  }
  .art--island { width: 54px; margin-left: 6px; background: linear-gradient(90deg, var(--palm) 0%, var(--palm) 45%, var(--sun) 60%, var(--sea) 100%); }
  .art--bird { width: 24px; height: 12px; margin-left: 10px; background: linear-gradient(90deg, var(--sun), var(--brand-orange)); }
  .art--waves { width: 60px; height: 12px; margin-left: 14px; background: linear-gradient(90deg, var(--sea), #5fb4e6); }
  .art--palms { width: 42px; margin-left: 4px; background: linear-gradient(90deg, var(--palm), #a9d86e, var(--brand-orange)); }
  .brand-name {
    font-family: "Ubuntu", sans-serif;
    font-weight: 700;
    font-size: 15px;
    color: var(--brand-green);
    margin-left: 12px;
    letter-spacing: -0.3px;
  }
  .brand-claim {
    font-family: "Ubuntu", sans-serif;
    font-weight: 400;
    font-size: 13px;
    color: var(--brand-blue);
    margin-left: 8px;
    letter-spacing: 0.4px;
  }
  .message-script {
    font-family: "Kaushan Script", cursive;
    font-size: 15px;
    color: var(--brand-orange);
    margin: 0 8px 0 14px;
  }
  .message-bold {
    font-family: "Montserrat", sans-serif;
    font-weight: 800;
    font-size: 12.5px;
    margin: 0 14px 0 10px;
  }
  .message-bold .accent { color: var(--brand-orange); }
  .message-bold .lead { color: var(--brand-blue); }
  .message-cta {
    flex: 0 0 auto;
    width: 484px;
    height: 100%;
    background: var(--brand-blue);
    color: #fff;
    font-family: "Montserrat", sans-serif;
    font-weight: 800;
    font-size: 12.5px;
    letter-spacing: 1.6px;
    display: flex;
    align-items: center;
    justify-content: center;
    margin-left: 4px;
  }
</style>
</head>
<body>

  <!-- Logo-Laufband -->
  <div class="led-band">
    <div class="brand-unit">
      <span class="art art--island" role="img" aria-label="Illustration: Insel mit Haus, Palmen und Sonne"></span>
      <span class="art art--bird" role="img" aria-label="Illustration: fliegende Möwe"></span>
      <span class="brand-name">welmora</span>
      <span class="brand-claim">Hotels &amp; Resorts</span>
      <span class="art art--waves" role="img" aria-label="Illustration: Wellen"></span>
      <span class="art art--palms" role="img" aria-label="Illustration: Palmen und Möwe"></span>
    </div>
    <div class="brand-unit">
      <span class="art art--island" role="img" aria-label="Illustration: Insel mit Haus, Palmen und Sonne"></span>
      <span class="art art--bird" role="img" aria-label="Illustration: fliegende Möwe"></span>
      <span class="brand-name">welmora</span>
      <span class="brand-claim">Hotels &amp; Resorts</span>
      <span class="art art--waves" role="img" aria-label="Illustration: Wellen"></span>
      <span class="art art--palms" role="img" aria-label="Illustration: Palmen und Möwe"></span>
    </div>
    <div class="brand-unit">
      <span class="art art--island" role="img" aria-label="Illustration: Insel mit Haus, Palmen und Sonne"></span>
      <span class="art art--bird" role="img" aria-label="Illustration: fliegende Möwe"></span>
      <span class="brand-name">welmora</span>
      <span class="brand-claim">Hotels &amp; Resorts</span>
      <span class="art art--waves" role="img" aria-label="Illustration: Wellen"></span>
      <span class="art art--palms" role="img" aria-label="Illustration: Palmen und Möwe"></span>
    </div>
  </div>

  <!-- Kurzurlaub-Slogan -->
  <div class="led-band">
    <div class="brand-unit">
      <span class="art art--island" role="img" aria-label="Illustration: Insel mit Haus, Palmen und Sonne"></span>
      <span class="art art--bird" role="img" aria-label="Illustration: fliegende Möwe"></span>
      <span class="brand-name">welmora</span>
      <span class="brand-claim">Hotels &amp; Resorts</span>
      <span class="art art--waves" role="img" aria-label="Illustration: Wellen"></span>
      <span class="art art--palms" role="img" aria-label="Illustration: Palmen und Möwe"></span>
    </div>
    <span class="art art--island" role="img" aria-label="Illustration: Insel mit Haus, Palmen und Sonne"></span>
    <span class="message-script">Jetzt Buchen Fur Ihren Nachsten Kurzurlaub...</span>
    <div class="brand-unit">
      <span class="art art--bird" role="img" aria-label="Illustration: fliegende Möwe"></span>
      <span class="brand-name">welmora</span>
      <span class="brand-claim">Hotels &amp; Resorts</span>
      <span class="art art--waves" role="img" aria-label="Illustration: Wellen"></span>
      <span class="art art--palms" role="img" aria-label="Illustration: Palmen und Möwe"></span>
    </div>
  </div>

  <!-- Regionen-Botschaft -->
  <div class="led-band">
    <div class="brand-unit">
      <span class="art art--island" role="img" aria-label="Illustration: Insel mit Haus, Palmen und Sonne"></span>
      <span class="art art--bird" role="img" aria-label="Illustration: fliegende Möwe"></span>
      <span class="brand-name">welmora</span>
      <span class="brand-claim">Hotels &amp; Resorts</span>
      <span class="art art--waves" role="img" aria-label="Illustration: Wellen"></span>
    </div>
    <span class="message-bold"><span class="accent">22X FUR SIE IN OST - </span>&nbsp;<span class="lead">DEUTSCHLANDS SCHONSTEN REGIONEN</span></span>
    <div class="brand-unit">
      <span class="art art--bird" role="img" aria-label="Illustration: fliegende Möwe"></span>
      <span class="brand-name">welmora</span>
      <span class="brand-claim">Hotels &amp; Resorts</span>
      <span class="art art--waves" role="img" aria-label="Illustration: Wellen"></span>
      <span class="art art--palms" role="img" aria-label="Illustration: Palmen und Möwe"></span>
    </div>
  </div>

  <!-- Buchungsaufruf -->
  <div class="led-band">
    <div class="brand-unit">
      <span class="art art--island" role="img" aria-label="Illustration: Insel mit Haus, Palmen und Sonne"></span>
      <span class="art art--bird" role="img" aria-label="Illustration: fliegende Möwe"></span>
      <span class="brand-name">welmora</span>
      <span class="brand-claim">Hotels &amp; Resorts</span>
      <span class="art art--waves" role="img" aria-label="Illustration: Wellen"></span>
    </div>
    <div class="message-cta">JETZT BUCHEN AUF WWW.WELMORA-HOTELS.DE</div>
    <div class="brand-unit">
      <span class="art art--bird" role="img" aria-label="Illustration: fliegende Möwe"></span>
      <span class="brand-name">welmora</span>
      <span class="brand-claim">Hotels &amp; Resorts</span>
      <span class="art art--waves" role="img" aria-label="Illustration: Wellen"></span>
      <span class="art art--palms" role="img" aria-label="Illustration: Palmen und Möwe"></span>
    </div>
  </div>

</body>
</html>
```